RZO Design tag

Looking to design a tag for our new hat & glove brand RZO Design. These are winter hats & gloves. Long story short these are lower cost/retail items but I'm trying to convey higher quality goods through a nice tag. I’ve attached a tag of another brand we have to give you a general idea of what I’d be looking for- but again for our new brand RZO Design.
I’m thinking we can do one general design- and then do it in 4 different color schemes: First one mimicking the attachment’s colors for ladies items- so a few different shades of pink. Then 2nd color scheme a darker more masculine color tone for mens or unisex items- maybe blue/dark blue, and then a 3rd color scheme for kids items that is more vibrant/kid like colors. Last one red & green for some Christmas items we do.
A few things:
• Trying to make the tags look classy as possible
• The tag will need to measure 2.25” high x 2” wide. The top little bit would have to be space left blank for a hole punch- just like on the attached sample tag. But again the tags designed would need to be 2.25" tall x 2" wide so not the same shape as the sample tag.
• For item name you can just put “Knit Hat” for the generic tag item name (in place of what says on the same “Chenille Slipper Bootie”). Please try to keep the writing a nice font similar to what is on this tag- again trying to have a classy tag look
• On the bottom center (In place of Made in China) it would just need to say “One Size” in standard font
Hope this helps & thank you
Target Market(s)
People buying winter hats & gloves
Industry/Entity Type
Retail- winter hats & gloves
Look and feel

```html
<!DOCTYPE html>
<html lang="en">
<head>
<meta charset="utf-8">
<title>Knit Hat Tags</title>
<link href="https://fonts.googleapis.com/css2?family=Comfortaa:wght@700&family=Arimo:wght@700&display=swap" rel="stylesheet">
<style>
  :root {
    --backdrop: #5c5c5c;
    --tag-light: #e4e4e4;
    --text-light: #ffffff;
    --pink-main: #d4005f;
    --pink-soft: #e2628f;
    --blue-main: #062f8e;
    --blue-soft: #5f86d8;
    --green-main: #2cb52c;
    --red-main: #e8101a;
  }
  html, body {
    margin: 0;
    padding: 0;
    width: 1200px;
    height: 965px;
    overflow: hidden;
    background: var(--backdrop);
  }
  .canvas {
    position: relative;
    width: 1200px;
    height: 965px;
  }
  .tag {
    position: absolute;
    width: 250px;
    height: 275px;
    background: linear-gradient(135deg, var(--stripe) 0%, var(--tag-light) 45%, var(--stripe) 100%);
    box-sizing: border-box;
  }
  .tag--ladies  { left: 352px; top: 272px; --stripe: var(--pink-soft); --hat: var(--pink-main); --band: var(--pink-soft); }
  .tag--mens    { left: 658px; top: 258px; --stripe: var(--blue-soft); --hat: var(--blue-main); --band: var(--blue-soft); }
  .tag--holiday { left: 438px; top: 572px; --stripe: var(--green-main); --hat: var(--red-main); --band: var(--green-main); }

  .tag__punch {
    position: absolute;
    left: 50%;
    top: 10px;
    width: 12px;
    height: 12px;
    margin-left: -6px;
    border-radius: 50%;
    background: var(--backdrop);
  }
  .tag__hat-art {
    position: absolute;
    left: 24px;
    top: 28px;
    width: 202px;
    height: 226px;
    border-radius: 60px 60px 18px 18px;
    background: linear-gradient(180deg, var(--hat) 0%, var(--hat) 62%, var(--band) 70%, var(--band) 100%);
  }
  .tag__name {
    position: absolute;
    left: 0;
    right: 0;
    top: 96px;
    margin: 0;
    text-align: center;
    font-family: "Comfortaa", sans-serif;
    font-weight: 700;
    font-size: 34px;
    line-height: 30px;
    color: var(--text-light);
  }
  .tag__name span { display: block; }
  .tag__size {
    position: absolute;
    left: 0;
    right: 0;
    bottom: 36px;
    margin: 0;
    text-align: center;
    font-family: "Arimo", sans-serif;
    font-weight: 700;
    font-size: 13px;
    color: var(--text-light);
  }
</style>
</head>
<body>
<main class="canvas">
  <article class="tag tag--ladies">
    <div class="tag__hat-art" role="img" aria-label="Illustration of a pink knit hat with a flower pompom"></div>
    <div class="tag__punch"></div>
    <h2 class="tag__name"><span>Knit</span><span>Hat</span></h2>
    <p class="tag__size">One Size</p>
  </article>

  <article class="tag tag--mens">
    <div class="tag__hat-art" role="img" aria-label="Illustration of a dark blue knit hat with a flower pompom"></div>
    <div class="tag__punch"></div>
    <h2 class="tag__name"><span>Knit</span><span>Hat</span></h2>
    <p class="tag__size">One Size</p>
  </article>

  <article class="tag tag--holiday">
    <div class="tag__hat-art" role="img" aria-label="Illustration of a red knit hat with green brim and flower pompom"></div>
    <div class="tag__punch"></div>
    <h2 class="tag__name"><span>Knit</span><span>Hat</span></h2>
    <p class="tag__size">One Size</p>
  </article>
</main>
</body>
</html>
```